LANDCAPE Business Card Design

We need a business card design close to what we are sending you, just more professional. We are a landscape management company located on Topsail Island so an island theme would be great. We would like to stay with a black background and bright green lettering. Something to stand out.

Target Market(s)

Commercial and private property owners

Industry/Entity Type

Landscape

Contact Information for Business Card

BRACKENFORD GROUNDS CARE, LLC,ENJOY YOUR OWN GREEN SANCTUARY, WADE PELLIN 336-555-0184, MILES DORAHT 910-555-0137

Font styles to use
Sans Serif

```html
<!DOCTYPE html>
<html lang="en">
<head>
<meta charset="utf-8">
<title>Brackenford Grounds Care – Business Card</title>
<link href="https://fonts.googleapis.com/css2?family=Open+Sans:wght@600;700;800&display=swap" rel="stylesheet">
<style>
  :root {
    --backdrop: #a9a9a9;
    --card-black: #050505;
    --card-green: #12963f;
    --swoosh-dark: #0b6a2c;
    --brand-green: #159443;
    --text-white: #ffffff;
    --text-black: #0a0a0a;
    --palm-tint: rgba(190, 240, 200, 0.45);
  }
  * { margin: 0; padding: 0; box-sizing: border-box; }
  html, body { width: 1200px; height: 900px; overflow: hidden; }
  body {
    background: var(--backdrop);
    font-family: "Open Sans", Arial, sans-serif;
    position: relative;
  }

  .brand-mark {
    position: absolute;
    left: 90px;
    top: 175px;
    width: 460px;
    display: flex;
    align-items: center;
    gap: 16px;
  }
  .brand-mark__dot {
    width: 22px; height: 22px;
    border-radius: 50%;
    background: var(--brand-green);
    flex: none;
  }
  .brand-mark__name {
    color: var(--brand-green);
    font-weight: 800;
    font-size: 30px;
    letter-spacing: 2px;
    line-height: 1.15;
  }

  .business-card {
    position: absolute;
    left: 480px;
    top: 440px;
    width: 620px;
    height: 340px;
    overflow: hidden;
    background: var(--card-green);
  }
  .business-card__bg { position: absolute; inset: 0; }

  .business-card__brand {
    position: absolute;
    left: 0; right: 0;
    top: 62px;
    text-align: center;
    color: var(--brand-green);
    font-weight: 800;
    font-size: 24px;
    letter-spacing: 2px;
  }

  .business-card__palms {
    position: absolute;
    right: 14px;
    bottom: 20px;
    width: 170px;
    height: 140px;
    background: linear-gradient(180deg, var(--palm-tint), rgba(190, 240, 200, 0.15));
    border-radius: 50% 50% 6px 6px / 40% 40% 6px 6px;
  }

  .contacts {
    position: absolute;
    left: 60px;
    top: 190px;
    display: flex;
    gap: 50px;
  }
  .contact__name {
    color: var(--text-white);
    font-weight: 700;
    font-size: 18px;
  }
  .contact__phone {
    color: var(--text-white);
    font-weight: 700;
    font-size: 14px;
    margin-top: 2px;
  }

  .tagline {
    position: absolute;
    left: 40px;
    bottom: 30px;
    color: var(--text-black);
    font-weight: 800;
    font-size: 16px;
    letter-spacing: 2px;
  }
</style>
</head>
<body>

  <div class="brand-mark">
    <span class="brand-mark__dot"></span>
    <span class="brand-mark__name">BRACKENFORD<br>GROUNDS CARE, LLC</span>
  </div>

  <section class="business-card">
    <svg class="business-card__bg" viewBox="0 0 620 340" preserveAspectRatio="none" aria-hidden="true">
      <rect width="620" height="340" fill="var(--card-green)"/>
      <path d="M0 60 Q330 200 620 150 V158 Q330 215 0 82 Z" fill="var(--swoosh-dark)"/>
      <path d="M0 0 H620 V148 Q330 195 0 56 Z" fill="var(--card-black)"/>
    </svg>

    <div class="business-card__brand">BRACKENFORD GROUNDS CARE, LLC</div>

    <div class="business-card__palms" role="img" aria-label="Faint palm tree silhouettes"></div>

    <div class="contacts">
      <div class="contact">
        <div class="contact__name">MILES DORAHT</div>
        <div class="contact__phone">910-555-0137</div>
      </div>
      <div class="contact">
        <div class="contact__name">WADE PELLIN</div>
        <div class="contact__phone">336-555-0184</div>
      </div>
    </div>

    <div class="tagline">ENJOY YOUR OWN GREEN SANCTUARY</div>
  </section>

</body>
</html>
```